Kestrel Summit 2019 Enemies of the End-Times Church Flyer

We want a church conference flyer designed. We are looking for a professional, yet catchy design that uses our brand colors and logo creatively while communicating key information of the event effectively. <br/>The flyer must include all of the following:<br/>Title: Kestrel Summit 2019<br/>Topic: The Enemies of The End-Times Church <br/>Subtitles: <br/> -How the antichrist raises an army by social behavior engineering. <br/>-How the architects of modern social constructs escaped the church's radar. <br/>-The Holy Spirit's end-times agenda:<br/> The Knock-Out Punch!<br/>Speaker: Prophet Marcus Toliver <br/>Dates/time: December 27, 28 & 29 at 6pm<br/>Location: Halvorn Community Center <br/> 241 Pellham Street <br/> Portland, ME 04102<br/>Contact info: phone: 207-555-0148 <br/>email: contact@brookmeadow.example <br/> www.vutel.example<br/>*The flyer must also include a picture of the speaker and our Vutel logo <br/>Thanks, we look forward to seeing what you come up with!

Colors

Designer to choose colors to be used in the design.

Requirements
Must have
• The flyer must include all of the following:
• Title: Kestrel Summit 2019
• Topic: The Enemies of The End-Times Church
• Subtitles:
• -How the antichrist raises an army by social behavior engineering.
• -How the architects of modern social constructs escaped the church's radar.
• -The Holy Spirit's end-times agenda:
• The Knock-Out Punch!
• Speaker: Prophet Marcus Toliver
• Dates/time: December 27, 28 & 29 at 6pm
• Location: Halvorn Community Center
• 241 Pellham Street
• Portland, ME 04102
• Contact info: phone: 207-555-0148
• email: contact@brookmeadow.example
• www.vutel.example
• *The flyer must also include a picture of the speaker and our Vutel logo
Should not have
• Pictures of crosses or church buildings

```html
<!DOCTYPE html>
<html lang="en">
<head>
<meta charset="utf-8">
<title>Kestrel Summit 2019 Flyer</title>
<link href="https://fonts.googleapis.com/css2?family=Barlow:wght@600;700&display=swap" rel="stylesheet">
<style>
  :root {
    --page: #ffffff;
    --navy-deep: #0c2238;
    --navy: #1b3f6b;
    --violet: #6a5d8e;
    --orange: #f39220;
    --white: #ffffff;
  }
  * { margin: 0; padding: 0; box-sizing: border-box; }
  html, body {
    width: 1200px; height: 1000px; overflow: hidden;
    background: var(--page);
    font-family: "Barlow", "Helvetica Neue", Arial, sans-serif;
  }
  .flyer {
    position: absolute; left: 227px; top: 17px;
    width: 742px; height: 960px; overflow: hidden;
    color: var(--white);
    background:
      radial-gradient(ellipse 380px 300px at 560px 300px, rgba(140,130,180,0.55), transparent 70%),
      radial-gradient(ellipse 420px 380px at 700px 560px, rgba(120,95,150,0.6), transparent 70%),
      linear-gradient(160deg, var(--navy) 0%, #24406a 35%, var(--violet) 70%, var(--navy-deep) 100%);
  }
  .flyer::after {
    content: ""; position: absolute; inset: 0;
    background: linear-gradient(90deg, rgba(8,24,40,0.55) 0%, transparent 55%);
    pointer-events: none;
  }
  .flyer > * { position: absolute; z-index: 1; }

  .brand { right: 34px; top: 72px; display: flex; align-items: center; gap: 10px; }
  .brand-dot { width: 22px; height: 22px; border-radius: 50%; background: var(--orange); }
  .brand-name { font-size: 46px; font-weight: 600; letter-spacing: 1px; color: var(--white); line-height: 1; }

  .title { left: 50px; top: 0; width: 700px; height: 400px; font-weight: 700; }
  .title span { position: absolute; left: 0; display: block; line-height: 1; white-space: nowrap; }
  .title-year { top: 113px; font-size: 84px; color: var(--white); }
  .title-main { top: 182px; font-size: 126px; color: var(--orange); }
  .title-sub { top: 307px; font-size: 80px; color: var(--orange); letter-spacing: 1px; }

  .topic { left: 56px; top: 404px; font-size: 22px; font-weight: 700; letter-spacing: 0.3px; }
  .points { left: 56px; top: 458px; list-style: none; font-size: 14.5px; font-weight: 700; line-height: 29px; }

  .schedule { left: 55px; top: 566px; font-size: 32px; font-weight: 700; line-height: 42px; }

  .speaker-photo {
    left: 52px; top: 693px; width: 146px; height: 146px; border-radius: 50%;
    background: radial-gradient(circle at 50% 45%, #7a5a4a 0%, #4a3a36 45%, #8a8f99 100%);
  }
  .speaker-name { left: 48px; top: 858px; font-size: 14.5px; font-weight: 700; }

  .corner { right: 0; bottom: 0; width: 469px; height: 444px; }
  .contact {
    right: 40px; top: 783px; text-align: right; font-style: normal;
    font-size: 15px; font-weight: 700; line-height: 21px;
  }
  .contact p + p { margin-top: 8px; }
</style>
</head>
<body>
  <main class="flyer">
    <div class="brand">
      <span class="brand-dot"></span>
      <span class="brand-name">Vutel</span>
    </div>

    <h1 class="title">
      <span class="title-year">2019</span>
      <span class="title-main">KESTREL</span>
      <span class="title-sub">SUMMIT</span>
    </h1>

    <h2 class="topic">THE ENEMIES OF THE END-TIMES CHURCH</h2>
    <ul class="points">
      <li>How the antichrist raises an army by social behavior engineering.</li>
      <li>How the architects of modern social constructs escaped the church's radar.</li>
      <li>The Holy Spirit's end-times agenda: The Knock-Out Punch!</li>
    </ul>

    <p class="schedule">DECEMBER 27, 28 &amp; 29<br>6pm</p>

    <div class="speaker-photo" role="img" aria-label="Portrait photo of the speaker"></div>
    <p class="speaker-name">Prophet Marcus Toliver</p>

    <svg class="corner" viewBox="0 0 469 444" aria-hidden="true">
      <polygon points="469,0 469,444 0,444" fill="var(--orange)"/>
    </svg>

    <address class="contact">
      <p>Halvorn Community Center<br>241 Pellham Street<br>Portland, ME 04102</p>
      <p>207-555-0148</p>
      <p>contact@brookmeadow.example<br>www.vutel.example</p>
    </address>
  </main>
</body>
</html>
```